FREE Network Assessment image for landing page

This graphic will be on a landing page and on the left will be Text and a download button that we change and control. The graphic for this project will be to the right.
I will add an example of the landing page area so that it makes more sense.

Please include the text from the sample - the font needs to be the same style as what we are using on the left side!

The graphic needs to be a .png file, roughly 713 x 527 white background. Use discretion on design layout.

Colors are black, Red = PMS 1795 and Gray = Cool Gray 10

Thanks,
Tom Farrow

Target Market(s)

small businesses

Industry/Entity Type

Information Technology

Font styles to use
Other font styles liked:
• See sample

Requirements
Must have
• see description
Nice to have
• Possibly small technology related image to help enhance the text but I don't want any image to compete with the text. Keep in mind the colors mentioned in the description - this is the web site colors.
Should not have
• Should not be hard to read

```html
<!DOCTYPE html>
<html lang="en">
<head>
<meta charset="utf-8">
<title>Free Network &amp; Computer Health Check Service</title>
<link href="https://fonts.googleapis.com/css2?family=Oswald:wght@400&family=Lato:wght@400;700&display=swap" rel="stylesheet">
<style>
  :root {
    --paper: #ffffff;
    --ink: #3f4043;
    --ink-dark: #1c1c1c;
    --accent: #f04b4b;
    --accent-text: #c4504f;
    --photo-dark: #5b5e66;
    --photo-mid: #b9b4ad;
    --photo-light: #e9e4dc;
  }
  * { box-sizing: border-box; margin: 0; padding: 0; }
  html, body { width: 1200px; height: 888px; overflow: hidden; background: var(--paper); }
  .canvas { position: relative; width: 1200px; height: 888px; background: var(--paper); overflow: hidden; }

  .headline {
    position: absolute; left: 56px; top: 40px;
    font-family: "Oswald", sans-serif; font-weight: 400;
    font-size: 76px; line-height: 84px; color: var(--ink);
    letter-spacing: -0.5px; text-transform: uppercase;
  }

  .features { position: absolute; left: 56px; top: 262px; list-style: none; }
  .feature { position: absolute; left: 0; display: flex; align-items: flex-start; width: 700px; }
  .feature-icon { width: 56px; height: 56px; flex: none; }
  .feature-text {
    margin-left: 25px; margin-top: -4px;
    font-family: "Lato", sans-serif; font-size: 27px; line-height: 34px;
    color: var(--accent-text);
  }
  .feature:nth-child(1) { top: 0; }
  .feature:nth-child(2) { top: 104px; }
  .feature:nth-child(3) { top: 209px; }
  .feature:nth-child(4) { top: 278px; }
  .feature:nth-child(5) { top: 385px; }

  .cta {
    position: absolute; left: 57px; top: 760px; width: 468px; height: 76px;
    border-radius: 38px; background: var(--accent); color: var(--paper);
    font-family: "Oswald", sans-serif; font-size: 34px; line-height: 76px;
    text-align: center; text-transform: uppercase; text-decoration: none;
  }

  .hero-photo {
    position: absolute; left: 506px; top: 326px; width: 694px; height: 562px;
    background: linear-gradient(160deg, var(--photo-light) 0%, var(--photo-mid) 45%, var(--photo-dark) 100%);
    clip-path: polygon(262px 0, 694px 0, 694px 562px, 0 562px, 0 480px, 262px 380px);
  }
</style>
</head>
<body>
<main class="canvas">
  <h1 class="headline">Free Network &amp;<br>Computer Health Check Service</h1>

  <ul class="features">
    <li class="feature">
      <svg class="feature-icon" viewBox="0 0 56 56" aria-hidden="true">
        <circle cx="22" cy="22" r="16" fill="none" stroke="var(--ink-dark)" stroke-width="4"/>
        <line x1="34" y1="34" x2="50" y2="50" stroke="#999" stroke-width="7" stroke-linecap="round"/>
        <ellipse cx="22" cy="23" rx="6" ry="8" fill="var(--accent)"/>
        <path d="M14 17l4 3M30 17l-4 3M13 25h5M31 25h-5M14 32l4-3M30 32l-4-3" stroke="var(--ink-dark)" stroke-width="2"/>
      </svg>
      <span class="feature-text">Check your network’s security against hacker<br>attacks, theft, ransomware, viruses, and more.</span>
    </li>
    <li class="feature">
      <svg class="feature-icon" viewBox="0 0 56 56" aria-hidden="true">
        <rect x="2" y="4" width="52" height="48" fill="#fff" stroke="var(--ink-dark)" stroke-width="3"/>
        <rect x="2" y="4" width="52" height="7" fill="var(--ink-dark)"/>
        <circle cx="28" cy="32" r="12" fill="var(--accent)"/>
        <circle cx="28" cy="32" r="4" fill="var(--ink-dark)"/>
        <path d="M28 15v4M28 45v4M11 32h4M41 32h4" stroke="var(--ink-dark)" stroke-width="2"/>
      </svg>
      <span class="feature-text">See who and what has access to your<br>network and data.</span>
    </li>
    <li class="feature">
      <svg class="feature-icon" viewBox="0 0 56 56" aria-hidden="true">
        <rect x="2" y="4" width="52" height="48" fill="#fff" stroke="var(--ink-dark)" stroke-width="3"/>
        <rect x="2" y="4" width="52" height="7" fill="var(--ink-dark)"/>
        <circle cx="28" cy="33" r="14" fill="var(--accent)"/>
        <line x1="28" y1="33" x2="28" y2="21" stroke="#fff" stroke-width="3"/>
      </svg>
      <span class="feature-text">Perform network and Internet speed test</span>
    </li>
    <li class="feature">
      <svg class="feature-icon" viewBox="0 0 56 56" aria-hidden="true">
        <rect x="3" y="6" width="50" height="36" rx="2" fill="#fff" stroke="var(--ink-dark)" stroke-width="4"/>
        <path d="M20 52h16M28 42v10" stroke="var(--ink-dark)" stroke-width="4"/>
        <circle cx="28" cy="24" r="10" fill="var(--accent)"/>
        <rect x="23" y="22" width="10" height="7" fill="var(--ink-dark)"/>
      </svg>
      <span class="feature-text">Resolve PC slowness issues, security<br>vulnerabilities and improper configurations</span>
    </li>
    <li class="feature">
      <svg class="feature-icon" viewBox="0 0 56 56" aria-hidden="true">
        <rect x="3" y="6" width="50" height="36" rx="2" fill="var(--ink-dark)"/>
        <path d="M20 52h16M28 42v10" stroke="var(--ink-dark)" stroke-width="4"/>
        <rect x="8" y="11" width="40" height="26" fill="var(--accent)"/>
        <circle cx="18" cy="22" r="6" fill="none" stroke="#fff" stroke-width="2"/>
        <path d="M30 33v-6M36 33v-10M42 33v-14" stroke="#fff" stroke-width="3"/>
      </svg>
      <span class="feature-text">Validate your backups are working and<br>recoverable in a timely fashion.</span>
    </li>
  </ul>

  <a class="cta" href="#book">Book an appointment now!</a>

  <div class="hero-photo" role="img" aria-label="Photo of a cheerful IT technician in a red cape and aviator cap raising a fist, seated at a wooden desk with a laptop, clipboard and glass of orange juice"></div>
</main>
</body>
</html>
```